Vibrant, yet professional, stationery set and other designs required.

I need to source a fantastic designer for a new project as part of my company using a new logo designed via pixel harbor.

**UPDATE** I am not looking for just 'fine' design that will suffice. I am looking for something great.

We are a life assurance brokerage based in Dublin, Ireland and HearthGuard.ie is our new website aimed at providing services for young families in Ireland. We are hoping to be the 'Vorn' level of service providers in this area and I am looking for the quality of design to reflect this :-) Hopefully that makes sense!

I have a preference for straight lines over curves and waves.

I need...

1. Business card
2. Letterhead
3. Banner (for printing - 76cm X 305cm)
4. Car branding for ZELKA 300 (2014 sport model) I believe the templates are freely available online.

Target Market(s)

Parents in Ireland - Aged 27 to 50.

Industry/Entity Type

Financial Planning

Colors

Designer to choose colors to be used in the design.

Requirements
Must have
• All of the items listed in the description above. I like clean, bright, legible, vibrant and professional design.
Should not have
• No silly or 'cheap' looking designs. This is a professional company looking to provide a professional service.

```html
<!DOCTYPE html>
<html lang="en">
<head>
<meta charset="utf-8">
<title>HearthGuard.ie – Business Card</title>
<link rel="stylesheet" href="https://fonts.googleapis.com/css2?family=Open+Sans:wght@400;600;700&display=swap">
<style>
  :root {
    --backdrop: #e6e4e1;
    --card: #1c1d1f;
    --card-edge: #2a2b2e;
    --logo-grey: #8c9196;
    --name-blue: #4cb6de;
    --title-green: #8cc63e;
    --text-white: #f2f2f2;
    --icon-blue: #4cb6de;
    --divider: #9a9ea3;
  }
  * { margin: 0; padding: 0; box-sizing: border-box; }
  html, body {
    width: 1200px;
    height: 864px;
    overflow: hidden;
    background: var(--backdrop);
    font-family: "Open Sans", sans-serif;
  }
  .canvas {
    position: relative;
    width: 1200px;
    height: 864px;
  }
  .card {
    position: absolute;
    width: 560px;
    height: 310px;
    background: var(--card);
    border: 1px solid var(--card-edge);
    border-radius: 4px;
    box-shadow: 0 10px 26px rgba(0, 0, 0, 0.28);
  }
  .card--front { left: 40px; top: 90px; }
  .card--back { left: 600px; top: 440px; }

  .brand {
    position: absolute;
    display: flex;
    align-items: center;
    color: var(--logo-grey);
    font-weight: 700;
    letter-spacing: -0.5px;
  }
  .brand__dot {
    flex: none;
    border-radius: 50%;
    background: var(--logo-grey);
  }
  .brand__name { line-height: 0.95; }

  .card--front .brand {
    left: 120px;
    top: 74px;
    gap: 18px;
    font-size: 64px;
  }
  .card--front .brand__dot { width: 22px; height: 22px; }

  .card--back .brand {
    left: 36px;
    top: 112px;
    gap: 12px;
    font-size: 38px;
  }
  .card--back .brand__dot { width: 13px; height: 13px; }

  .divider {
    position: absolute;
    left: 276px;
    top: 44px;
    width: 1px;
    height: 222px;
    background: linear-gradient(to bottom, transparent, var(--divider) 20%, var(--divider) 80%, transparent);
  }
  .contact {
    position: absolute;
    left: 298px;
    top: 62px;
    color: var(--text-white);
    font-size: 15px;
    line-height: 19px;
  }
  .contact__name {
    color: var(--name-blue);
    font-weight: 700;
    font-size: 16px;
    letter-spacing: 0.3px;
  }
  .contact__title {
    color: var(--title-green);
    font-weight: 600;
    font-size: 15px;
  }
  .contact__address { margin-bottom: 2px; }
  .contact__list { list-style: none; }
  .contact__item {
    display: flex;
    align-items: center;
    gap: 9px;
    height: 19px;
  }
  .contact__icon {
    width: 12px;
    height: 12px;
    flex: none;
    fill: var(--icon-blue);
  }
</style>
</head>
<body>
<main class="canvas">

  <section class="card card--front" aria-label="Business card front">
    <div class="brand">
      <span class="brand__dot"></span>
      <span class="brand__name">Hearth<br>Guard.ie</span>
    </div>
  </section>

  <section class="card card--back" aria-label="Business card back">
    <div class="brand">
      <span class="brand__dot"></span>
      <span class="brand__name">Hearth<br>Guard.ie</span>
    </div>

    <div class="divider"></div>

    <div class="contact">
      <p class="contact__name">AIDEN WALSH</p>
      <p class="contact__title">CEO/FOUNDER</p>
      <p class="contact__address">42 Larch Row<br>Ranelagh, Dublin D06 K7P2</p>
      <ul class="contact__list">
        <li class="contact__item">
          <svg class="contact__icon" viewBox="0 0 12 12" aria-hidden="true"><path d="M1 4c0-2 2-3 5-3s5 1 5 3l-2 1-1-1.5H4L3 5zM3 6h6l1 5H2z"/></svg>
          <span>01 496 0271</span>
        </li>
        <li class="contact__item">
          <svg class="contact__icon" viewBox="0 0 12 12" aria-hidden="true"><path d="M3 0h6v12H3zM4 1.5v8h4v-8z"/></svg>
          <span>087 555 0193</span>
        </li>
        <li class="contact__item">
          <svg class="contact__icon" viewBox="0 0 12 12" aria-hidden="true"><path d="M3 0h6v4H3zM0 5h12v6H0zM2 7v2h8V7z"/></svg>
          <span>01 496 0288</span>
        </li>
        <li class="contact__item">
          <svg class="contact__icon" viewBox="0 0 12 12" aria-hidden="true"><path d="M0 2h12v8H0zM1 3l5 4 5-4z"/></svg>
          <span>aiden@hearthguard.ie</span>
        </li>
        <li class="contact__item">
          <svg class="contact__icon" viewBox="0 0 12 12" aria-hidden="true"><circle cx="6" cy="6" r="5.5"/><path d="M0.5 6h11M6 0.5v11" stroke="#1c1d1f" stroke-width="1"/></svg>
          <span>www.hearthguard.ie</span>
        </li>
      </ul>
    </div>
  </section>

</main>
</body>
</html>
```